Craft oriented film company needs a Business Card design

Hi all,
We're a 2-man band film company in New Zealand called Kestrel Pictures. We're good honest blokes, who are very passionate about the craft of film making. I've attached our current logo which has a bit of a crafty/artisan feel that we like. Feel free to use it - or throw the baby out with the bathwater and start again..... you never know, you might inspire a complete brand re-work.

In any case, the vibe we want to give out is that we are solid, dependable and no bullshit - but without compromising creative excellence and being in the now. We like the 'Brooklyn' artisan style of work.

Preferably single sided.

We need the standard stuff:
Name, job title, cellphone, email address and physical address (this can be smaller if you like - street, suburb, city & zip, country [if you want])

Check out our website to learn more about us: kestrelpictures.example

Target Market(s)

Brand marketers and advertising agency creatives looking for video production.

Industry/Entity Type

Baby

Requirements
Should not have
• Nothing flashy or too 'futuristic', we want it to feel grounded and real. A limited colour palette is preferred.
We don't want any film reels or cameras or anything obvious like that.

```html
<!DOCTYPE html>
<html lang="en">
<head>
<meta charset="utf-8">
<title>Kestrel Pictures — Business Card</title>
<link rel="stylesheet" href="https://fonts.googleapis.com/css2?family=Arimo:wght@400;700&display=swap">
<style>
  :root {
    --backdrop: #d8d3cb;
    --card: #ffffff;
    --card-edge: #5a5a5a;
    --ink: #111111;
    --text: #4a4a4a;
    --muted: #5c5c5c;
    --rule: #c9c9c9;
  }
  * { margin: 0; padding: 0; box-sizing: border-box; }
  html, body {
    width: 1200px;
    height: 755px;
    overflow: hidden;
    background: var(--backdrop);
    font-family: "Arimo", Arial, sans-serif;
  }
  .card {
    position: absolute;
    left: 80px;
    top: 78px;
    width: 1040px;
    height: 600px;
    background: var(--card);
    border: 3px solid var(--card-edge);
    box-shadow: 0 6px 18px rgba(0, 0, 0, 0.18);
  }
  .brand {
    position: absolute;
    left: 56px;
    top: 112px;
    display: flex;
    align-items: center;
    gap: 26px;
  }
  .brand-disc {
    width: 150px;
    height: 150px;
    border-radius: 50%;
    background: var(--ink);
    flex: none;
  }
  .brand-name {
    font-size: 42px;
    font-weight: 700;
    color: var(--ink);
    line-height: 1;
  }
  .holder {
    position: absolute;
    right: 48px;
    text-align: right;
    line-height: 1;
  }
  .holder-name {
    top: 310px;
    font-size: 40px;
    font-weight: 700;
    color: var(--text);
  }
  .holder-title {
    top: 378px;
    font-size: 24px;
    color: var(--muted);
  }
  .divider {
    position: absolute;
    left: 20px;
    right: 20px;
    top: 368px;
    height: 3px;
    background: linear-gradient(to right, rgba(201,201,201,0), var(--rule) 20%, #b5b5b5 50%, var(--rule) 80%, rgba(201,201,201,0));
  }
  .contacts {
    position: absolute;
    left: 56px;
    top: 406px;
    list-style: none;
  }
  .contact {
    display: flex;
    align-items: center;
    gap: 12px;
    height: 28px;
    margin-bottom: 29px;
    font-size: 28px;
    color: var(--text);
    line-height: 1;
  }
  .contact svg {
    width: 20px;
    height: 22px;
    flex: none;
    fill: var(--text);
  }
  .address {
    position: absolute;
    right: 48px;
    top: 484px;
    text-align: right;
    font-style: normal;
    font-size: 27px;
    line-height: 36px;
    color: var(--text);
  }
</style>
</head>
<body>
  <main class="card">
    <div class="brand">
      <span class="brand-disc"></span>
      <span class="brand-name">Kestrel Pictures</span>
    </div>

    <h1 class="holder holder-name">Your Name</h1>
    <div class="divider"></div>
    <p class="holder holder-title">Title</p>

    <ul class="contacts">
      <li class="contact">
        <svg viewBox="0 0 20 22" aria-hidden="true"><path d="M5 1h10a2 2 0 0 1 2 2v16a2 2 0 0 1-2 2H5a2 2 0 0 1-2-2V3a2 2 0 0 1 2-2zm1 3v9h8V4H6zm2 12v2h4v-2H8z"/></svg>
        (123) 456-7890
      </li>
      <li class="contact">
        <svg viewBox="0 0 20 22" aria-hidden="true"><path d="M1 6h18v12H1zM2.5 7.5 10 13l7.5-5.5" /><path d="M1 6l9 7 9-7" fill="none" stroke="#fff" stroke-width="1.6"/></svg>
        Info@kestrelpictures.example
      </li>
      <li class="contact">
        <svg viewBox="0 0 20 22" aria-hidden="true"><g fill="none" stroke="#4a4a4a" stroke-width="1.6"><circle cx="10" cy="11" r="8"/><ellipse cx="10" cy="11" rx="3.5" ry="8"/><path d="M2 11h16M3.5 6.5h13M3.5 15.5h13"/></g></svg>
        www.kestrelpictures.example
      </li>
    </ul>

    <address class="address">
      street, suburb, city<br>
      zip, country
    </address>
  </main>
</body>
</html>
```